Mosvane Design

Looking for Mosvane banner and square design:
Mosvane Banner
W:1600 px H:400 px
Square
120x120

Logo attached.

Description: Data-Driven stock market portfolio management using quantitative analysis.

```html
<!DOCTYPE html>
<html lang="en">
<head>
<meta charset="utf-8">
<title>Mosvane – Rules-based Investing Banner</title>
<link rel="stylesheet" href="https://fonts.googleapis.com/css2?family=Heebo:wght@300;400;700&family=Montserrat:wght@500&display=swap">
<style>
  :root {
    --bg: #ffffff;
    --ink-headline: #2b5f80;
    --ink-strong: #0b4f82;
    --brand: #1c6fb3;
    --glow-left: rgba(120, 180, 240, 0.45);
    --glow-right: rgba(70, 110, 240, 0.75);
    --glow-violet: rgba(140, 70, 230, 0.55);
    --scene-base: #e8f1fa;
    --scene-mid: #c6dcf1;
    --scene-deep: #7fa9d6;
    --scene-navy: #2a3f6a;
    --circuit: rgba(190, 215, 235, 0.45);
  }
  * { margin: 0; padding: 0; box-sizing: border-box; }
  html, body { width: 1200px; height: 300px; overflow: hidden; background: var(--bg); }
  .banner {
    position: relative;
    width: 1200px;
    height: 300px;
    overflow: hidden;
    background:
      radial-gradient(ellipse 150px 190px at 10px 190px, var(--glow-left), transparent 70%),
      radial-gradient(ellipse 170px 220px at 1190px 170px, var(--glow-right), transparent 70%),
      radial-gradient(ellipse 120px 80px at 1180px 0, var(--glow-violet), transparent 70%),
      var(--bg);
  }
  .circuit-accent {
    position: absolute;
    left: 400px;
    top: -60px;
    width: 220px;
    height: 115px;
    border-radius: 0 0 115px 115px;
    border: 26px solid var(--circuit);
    border-top: none;
    transform: rotate(-8deg);
  }
  .brand {
    position: absolute;
    left: 143px;
    top: 30px;
    display: flex;
    align-items: center;
    gap: 10px;
    font-family: "Montserrat", sans-serif;
    font-weight: 500;
    color: var(--brand);
  }
  .brand-dot {
    width: 30px;
    height: 30px;
    border-radius: 50%;
    background: var(--brand);
  }
  .brand-name {
    font-size: 22px;
    letter-spacing: 0.06em;
    line-height: 1;
  }
  .headline {
    position: absolute;
    left: 142px;
    top: 101px;
    font-family: "Heebo", sans-serif;
    font-weight: 300;
    font-size: 36px;
    line-height: 48px;
    color: var(--ink-headline);
    letter-spacing: 0.01em;
  }
  .headline strong {
    display: block;
    font-weight: 700;
    color: var(--ink-strong);
  }
  .scene {
    position: absolute;
    left: 695px;
    top: 18px;
    width: 360px;
    height: 276px;
    border-radius: 32px;
    background:
      radial-gradient(ellipse 70px 55px at 205px 105px, var(--scene-navy), transparent 85%),
      radial-gradient(ellipse 150px 100px at 190px 140px, var(--scene-deep), transparent 80%),
      linear-gradient(160deg, var(--scene-base) 0%, var(--scene-mid) 100%);
    box-shadow: 0 10px 30px rgba(90, 140, 200, 0.18);
  }
</style>
</head>
<body>
  <main class="banner">
    <div class="circuit-accent" aria-hidden="true"></div>

    <header class="brand">
      <span class="brand-dot" aria-hidden="true"></span>
      <span class="brand-name">MOSVANE</span>
    </header>

    <h1 class="headline">
      Rules-based Investing<br>
      Strategies using
      <strong>Quantitative Analysis</strong>
    </h1>

    <div class="scene" role="img" aria-label="Isometric illustration of analysts working around floating platforms with data dashboards, charts and a server"></div>
  </main>
</body>
</html>
```